App UI Design: Shopping/E-commerce App

Project :
Develop an UI design & App icon for an E-commerce/Shopping App

About the App/ Target Audience:
This grocery & food shopping app will be used by independent pub, café, restaurant owners to place & manage their purchases of foods and groceries for their catering businesses.

They will use the app to access product catalogues & special promotions, search & buy large quantities of groceries or catering supplies, and the ability to manage and track status of their order.

The HTML5 App’s has been built with a very basic structure. It now needs the visual layer of the UI designed

Note:
The app is tailored for business & catering orders, not retail/supermarket buyers, so the visual needs to look smart & not too casual.
Updates

Reason: Current submissions have not met out expectations. Please use the similar app examples in the PDF as a strong point of reference for the look & feel. Feedback will be given as submissions come in, please feel free to submit initial concepts of 1 or 2 of the pages & we'll provide feedback on whether it is on the right track or not before you do more work. Current submission will also receive feedback in the next few days. We look forward to new submissions!

Target Market(s)

Male & Female. Independent pub, café, restaurant owners buying for their catering businesses. Chefs etc.

Industry/Entity Type

Restaurant

Requirements
Must have
• An overview of elements/pages of the app that needs to be designed are:
(DOWNLOAD a more detailed diagram PDF explanation)

1. Welcome- Log-in Page
2. Homepage – index that links to different function of the app

Products:
3. Promotions page – for products on special for a limited time
4. Catalogue page – access to a range of catalogue

Ways to buy:
5. Basket (Shopping Cart) - tracking items they are buying from the catalogues
6. Templates (Pre-set Shopping list)- Set shopping list that has been preloaded for certain menu
7. Open Order page

My Account:
8. My Account/profile page – Users can check the status of their order, look at past orders, look at their account number & details etc

_______________________________________________________

Icon set- Icons to represent each pages that act as visual cues for easier browsing.

2 Main features that need to be accessible & consistent throughout all pages are:
a) The Navigation Bar –
so the user can quickly find their way back & access to the main functions
b) The Search bar –
whether it drops down when needed, or is featured as a header/footer.
c) Log out button
Nice to have

Things to keep in mind:

The UI design essentially needs to be a customizable template that can easily adapt to any brand/logo with a slight change of the color scheme. As we will later implement our brand & logo onto it.

We’re looking for a clean & clear design that allows for a straight forward easy user experience.

You are free to develop different layout & UI pattern that you feel is the most efficient way the user can walk through the App & make their purchase in no more than 2 or 3 clicks
________________________________________________

Screenshot of Similar Apps for reference are also in the PDF

```html
<!DOCTYPE html>
<html lang="en">
<head>
<meta charset="utf-8">
<title>Catalogue</title>
<link rel="stylesheet" href="https://fonts.googleapis.com/css2?family=Arimo:wght@400;700&display=swap">
<style>
:root{
  --status-bg:#000;
  --blue-top:#5fb3f2;
  --blue-bottom:#2e8ee0;
  --blue-edge:#1f6fb8;
  --band:#2b2f34;
  --row-a:#f2f2f2;
  --row-b:#e9e9e9;
  --divider:#cfcfcf;
  --ink:#4a4a4a;
  --white:#fff;
  --tab-top:#3c3c3c;
  --tab-bottom:#1a1a1a;
  --tab-icon:#d9d9d9;
  --muted:#8a8a8a;
}
*{box-sizing:border-box;margin:0;padding:0}
html,body{width:800px;height:1200px;overflow:hidden;background:#fff}
body{font-family:"Arimo",Arial,sans-serif;position:relative}
.status-bar{position:absolute;top:0;left:0;width:800px;height:50px;background:var(--status-bg);color:var(--white)}
.status-time{position:absolute;width:100%;text-align:center;top:8px;font-size:31px;font-weight:700}
.status-signal{position:absolute;left:10px;top:13px}
.status-battery{position:absolute;right:12px;top:14px}
.app-header{position:absolute;top:50px;left:0;width:800px;height:113px;background:linear-gradient(var(--blue-top),var(--blue-bottom));border-top:1px solid #8ccaf7}
.app-title{position:absolute;width:100%;text-align:center;top:28px;color:var(--white);font-size:49px;font-weight:700;letter-spacing:.5px;text-shadow:0 -1px 1px rgba(0,0,0,.25)}
.header-btn{position:absolute;top:15px;width:112px;height:86px;border-radius:7px;background:linear-gradient(#4aa6ee,#2a86d6);border:2px solid var(--blue-edge);box-shadow:inset 0 1px 0 rgba(255,255,255,.35);display:flex;align-items:center;justify-content:center}
.header-btn.menu{left:13px}
.header-btn.search{right:13px}
.search-band{position:absolute;top:163px;left:0;width:800px;height:109px;background:var(--band);border-top:3px solid #1d2024}
.search-field{position:absolute;left:27px;top:19px;width:746px;height:72px;border-radius:36px;background:var(--white);box-shadow:inset 0 2px 4px rgba(0,0,0,.35)}
.search-field .lens{position:absolute;left:22px;top:18px}
.search-text{position:absolute;left:73px;top:17px;font-size:34px;color:#3a3a3a}
.search-text .caret{display:inline-block;width:2px;height:34px;background:#2e8ee0;vertical-align:-5px;margin-left:1px}
.search-clear{position:absolute;right:14px;top:13px}
.product-list{position:absolute;top:272px;left:0;width:800px;height:805px;overflow:hidden}
.product-row{position:relative;height:169px;border-bottom:2px solid var(--divider);background:var(--row-a)}
.product-row:nth-child(even){background:var(--row-b)}
.product-thumb{position:absolute;left:10px;top:21px;width:128px;height:128px;border-radius:6px;background:var(--white);border:1px solid #c8c8c8;padding:7px}
.product-thumb span{display:block;width:100%;height:100%}
.thumb-knives{background:linear-gradient(135deg,#e9e4dc,#8a6a48 60%,#2b2b2b)}
.thumb-cake{background:linear-gradient(160deg,#5b7a7e,#e8dfd0 45%,#3c2a22)}
.thumb-paprika{background:linear-gradient(135deg,#f3d21a,#e8b40f 55%,#b41a1a)}
.thumb-stirfry{background:linear-gradient(135deg,#4b3422,#b8462a 50%,#5e7a2c)}
.product-name{position:absolute;left:164px;top:26px;font-size:29px;font-weight:700;color:var(--ink)}
.price-line{position:absolute;left:164px;font-size:27px;color:var(--ink)}
.price-line b{font-weight:400;position:absolute;left:135px;white-space:nowrap}
.price-1{top:67px}
.price-2{top:106px}
.add-btn{position:absolute;left:690px;top:46px;width:100px;height:76px;border-radius:7px;background:linear-gradient(#58aef0,#2c8ade);border:1px solid var(--blue-edge);box-shadow:inset 0 1px 0 rgba(255,255,255,.35);display:flex;align-items:center;justify-content:center}
.tab-bar{position:absolute;bottom:0;left:0;width:800px;height:123px;display:flex;background:linear-gradient(var(--tab-top),var(--tab-bottom));border-top:2px solid #111}
.tab{flex:1;display:flex;align-items:center;justify-content:center;border-right:2px solid #0f0f0f;border-left:1px solid #4a4a4a}
.tab:last-child{border-right:none}
.tab.active{background:linear-gradient(#3a9ae6,#1d72c4)}
</style>
</head>
<body>
<div class="status-bar">
  <svg class="status-signal" width="50" height="24" viewBox="0 0 50 24" fill="#fff">
    <rect x="0" y="16" width="6" height="8"/><rect x="9" y="12" width="6" height="12"/><rect x="18" y="8" width="6" height="16"/><rect x="27" y="4" width="6" height="20"/><rect x="36" y="0" width="6" height="24"/>
  </svg>
  <div class="status-time">8:08 PM</div>
  <svg class="status-battery" width="50" height="24" viewBox="0 0 50 24">
    <rect x="1" y="1" width="42" height="22" rx="3" fill="none" stroke="#fff" stroke-width="2"/>
    <rect x="5" y="5" width="34" height="14" fill="#fff"/><rect x="44" y="8" width="4" height="8" fill="#fff"/>
  </svg>
</div>

<header class="app-header">
  <div class="header-btn menu">
    <svg width="42" height="32" viewBox="0 0 42 32" fill="#fff"><rect y="0" width="42" height="6" rx="1"/><rect y="13" width="42" height="6" rx="1"/><rect y="26" width="42" height="6" rx="1"/></svg>
  </div>
  <h1 class="app-title">Catalogue</h1>
  <div class="header-btn search">
    <svg width="44" height="44" viewBox="0 0 44 44"><circle cx="18" cy="18" r="12" fill="none" stroke="#fff" stroke-width="6"/><line x1="27" y1="27" x2="40" y2="40" stroke="#fff" stroke-width="8" stroke-linecap="round"/></svg>
  </div>
</header>

<div class="search-band">
  <div class="search-field">
    <svg class="lens" width="36" height="36" viewBox="0 0 36 36"><circle cx="14" cy="14" r="10" fill="none" stroke="var(--muted)" stroke-width="4"/><line x1="22" y1="22" x2="32" y2="32" stroke="var(--muted)" stroke-width="6" stroke-linecap="round"/></svg>
    <div class="search-text">Deliciou<span class="caret"></span></div>
    <svg class="search-clear" width="46" height="46" viewBox="0 0 46 46"><circle cx="23" cy="23" r="23" fill="#9a9a9a"/><path d="M15 15 31 31M31 15 15 31" stroke="#fff" stroke-width="5" stroke-linecap="round"/></svg>
  </div>
</div>

<main class="product-list">
  <div class="product-row">
    <div class="product-thumb"><span class="thumb-knives" role="img" aria-label="Photo of a kitchen knife set in a wooden block"></span></div>
    <div class="product-name">Kanto Kitchen Knife Sets</div>
    <div class="price-line price-1">2 singles:<b>$14.50</b></div>
    <div class="price-line price-2">3 cases:<b>$31.00</b></div>
    <div class="add-btn"><svg width="44" height="36" viewBox="0 0 44 36"><use href="#basket"/></svg></div>
  </div>
  <div class="product-row">
    <div class="product-thumb"><span class="thumb-cake" role="img" aria-label="Photo of a fruit-topped chocolate cake"></span></div>
    <div class="product-name">Organic Fruity Mocca Cake</div>
    <div class="price-line price-1">2 singles:<b>$14.50</b></div>
    <div class="price-line price-2">1 cases:<b>$22.00</b></div>
    <div class="add-btn"><svg width="44" height="36" viewBox="0 0 44 36"><use href="#basket"/></svg></div>
  </div>
  <div class="product-row">
    <div class="product-thumb"><span class="thumb-paprika" role="img" aria-label="Photo of red and yellow bell peppers"></span></div>
    <div class="product-name">Red Paprika &amp; Yellow Paprika</div>
    <div class="price-line price-1">1 singles:<b>$14.50</b></div>
    <div class="price-line price-2">2 cases:<b>$22.00</b></div>
    <div class="add-btn"><svg width="44" height="36" viewBox="0 0 44 36"><use href="#basket"/></svg></div>
  </div>
  <div class="product-row">
    <div class="product-thumb"><span class="thumb-stirfry" role="img" aria-label="Photo of a garlic stir-fry dish"></span></div>
    <div class="product-name">Chinese Food with Garlic</div>
    <div class="price-line price-1">2 singles:<b>$14.50</b></div>
    <div class="add-btn"><svg width="44" height="36" viewBox="0 0 44 36"><use href="#basket"/></svg></div>
  </div>
  <div class="product-row">
    <div class="product-thumb"><span class="thumb-knives" role="img" aria-label="Photo of a kitchen knife set in a wooden block"></span></div>
    <div class="product-name">Kanto Kitchen Knife Sets</div>
    <div class="price-line price-1">2 singles:<b>$14.50</b></div>
    <div class="price-line price-2">3 cases:<b>$31.00</b></div>
    <div class="add-btn"><svg width="44" height="36" viewBox="0 0 44 36"><use href="#basket"/></svg></div>
  </div>
</main>

<nav class="tab-bar">
  <div class="tab">
    <svg width="66" height="70" viewBox="0 0 66 70"><rect x="4" y="6" width="58" height="40" fill="var(--tab-icon)" stroke="#fff" stroke-width="2"/><rect x="28" y="0" width="10" height="6" fill="var(--tab-icon)"/><path d="M33 46 33 66M33 50 16 68M33 50 50 68" stroke="var(--tab-icon)" stroke-width="4"/><g fill="#333"><path d="M33 12l3 6 6 1-4.5 4 1 6-5.5-3-5.5 3 1-6-4.5-4 6-1z"/><path d="M19 24l2 4 4 .5-3 3 .8 4-3.8-2-3.8 2 .8-4-3-3 4-.5z"/><path d="M47 24l2 4 4 .5-3 3 .8 4-3.8-2-3.8 2 .8-4-3-3 4-.5z"/></g></svg>
  </div>
  <div class="tab active">
    <svg width="60" height="76" viewBox="0 0 60 76"><path d="M2 2H44L58 16V74H2Z" fill="#e9eef4" stroke="#fff" stroke-width="2"/><path d="M44 2V16H58" fill="#c9d3de"/><g fill="#3a86c8"><rect x="10" y="14" width="22" height="4"/><rect x="10" y="26" width="40" height="3"/><rect x="10" y="34" width="40" height="3"/><rect x="10" y="42" width="40" height="3"/><rect x="10" y="50" width="40" height="3"/><rect x="28" y="62" width="22" height="4"/></g></svg>
  </div>
  <div class="tab">
    <svg width="72" height="62" viewBox="0 0 44 36"><use href="#basket-grey"/></svg>
  </div>
  <div class="tab">
    <svg width="56" height="76" viewBox="0 0 56 76"><rect x="2" y="8" width="52" height="66" rx="3" fill="var(--tab-icon)"/><rect x="16" y="2" width="24" height="12" rx="3" fill="#999" stroke="#333" stroke-width="2"/><g fill="#333"><rect x="10" y="24" width="5" height="5"/><rect x="20" y="25" width="26" height="3"/><rect x="10" y="36" width="5" height="5"/><rect x="20" y="37" width="26" height="3"/><rect x="10" y="48" width="5" height="5"/><rect x="20" y="49" width="26" height="3"/><rect x="10" y="60" width="5" height="5"/><rect x="20" y="61" width="26" height="3"/></g></svg>
  </div>
  <div class="tab">
    <svg width="74" height="70" viewBox="0 0 74 70"><path d="M4 4H14L24 56H66" fill="none" stroke="var(--tab-icon)" stroke-width="5" stroke-linejoin="round"/><rect x="28" y="12" width="34" height="38" fill="var(--tab-icon)"/><path d="M45 22V40M38 29 45 22 52 29" stroke="#333" stroke-width="3" fill="none"/><circle cx="28" cy="62" r="6" fill="var(--tab-icon)"/><circle cx="60" cy="62" r="6" fill="var(--tab-icon)"/></svg>
  </div>
  <div class="tab">
    <svg width="66" height="74" viewBox="0 0 66 74"><ellipse cx="33" cy="22" rx="16" ry="20" fill="var(--tab-icon)"/><path d="M2 74C2 56 14 48 24 46L33 52 42 46C52 48 64 56 64 74Z" fill="var(--tab-icon)"/></svg>
  </div>
</nav>

<svg width="0" height="0" style="position:absolute">
  <defs>
    <g id="basket" fill="#fff">
      <path d="M14 10 24 2" stroke="#fff" stroke-width="3" stroke-linecap="round"/>
      <rect x="2" y="10" width="40" height="6" rx="2"/>
      <path d="M5 18H39L36 34H8Z"/>
      <g fill="#2e8ee0"><rect x="12" y="21" width="4" height="10" rx="1"/><rect x="20" y="21" width="4" height="10" rx="1"/><rect x="28" y="21" width="4" height="10" rx="1"/></g>
    </g>
    <g id="basket-grey" fill="var(--tab-icon)">
      <path d="M14 10 24 2" stroke="var(--tab-icon)" stroke-width="3" stroke-linecap="round"/>
      <rect x="2" y="10" width="40" height="6" rx="2"/>
      <path d="M5 18H39L36 34H8Z"/>
      <g fill="#2a2a2a"><rect x="12" y="21" width="4" height="10" rx="1"/><rect x="20" y="21" width="4" height="10" rx="1"/><rect x="28" y="21" width="4" height="10" rx="1"/></g>
    </g>
  </defs>
</svg>
</body>
</html>
```